K P Guard Services - Alarm and CCTV installation Flyer

Need a flyer designed that grabs the attention of potential customers, we need the price to stand out the most to grab people’s attention, whether they are residential or commercial.We are a security company based in Brentwood Essex but cover London and the home counties. here is our website to take a look at www.kpguardservices.co.uk. We want them to know we install complete alarm and Cctv systems and will keep them “safe”

Target Market(s)

residential and commercial property

Colors
f37122

Requirements
Must have
• on one side
• large clear logo - professional design
• - Intruder Alarms starting from £495 + VAT. (Big text)
• - £150 discount on installations
• *terms and conditions apply (small text)
• - Not happy with your current provider? Free of charge no obligation take over survey and quotation and up to £100 off
• - CCTV systems starting from £595 + VAT (based on 2 cameras)
• K P Guard Services are always there, always available, wherever and whenever you need us.
• Large telephone number at the bottom 01632 480913
• Address / email / website as a footer * see website for details
• on second side
• large and bold
• Are you looking to keep you and your premises safe?
• - K P Guard Services install, maintain and repair all intruder alarms, CCTV, intercom and access control
• - View, control and manage your security systems anywhere in the world
• - Feel at ease with monitoring services & police response tailored to suit you and your business
• - K P Guard can takeover any existing security system and offer maintenance checks to guarantee the best performance for you and your premises
• - K P Guard understand that being security conscious is ever increasing, protecting your property and family is a number one priority
• - Our fully insured and accredited team offer quality, safety and cost efficiency throughout the whole process
• - K P Guard Services are using the latest cloud-based technology to stay connected with your home and business 24/7
• If you are looking to improve the security in your home, office or commercial property then call a member of our team today for a free quote.
• Fully insured and accredited
• Jobrater logo and NQRB Intruder and CCTV logos
• Logo somewhere on page and
• Telephone number
• Address / email / website as footer
Nice to have
• We would like to have the text saying
• Intruder alarms installed from £495 + vat the biggest text on the page. Most likely the £495 part the largest.
• Also would like “not happy with your current provider” more obvious
• We would like use our company colours - Orange/White/black

```html
<!DOCTYPE html>
<html lang="en">
<head>
<meta charset="utf-8">
<title>K P Guard Services – Alarm and CCTV Flyer</title>
<link href="https://fonts.googleapis.com/css2?family=Open+Sans:wght@400;600;700;800&display=swap" rel="stylesheet">
<style>
  :root {
    --orange: #f37122;
    --red: #e32b2b;
    --dark: #3c3c3c;
    --ink: #2f2f2f;
    --white: #ffffff;
    --backdrop: #b4b4b4;
  }
  * { margin: 0; padding: 0; box-sizing: border-box; }
  html, body { width: 1200px; height: 1200px; overflow: hidden; }
  body {
    background: var(--backdrop);
    font-family: "Open Sans", Arial, sans-serif;
    color: var(--ink);
    position: relative;
  }
  .flyer {
    position: absolute;
    width: 680px;
    height: 965px;
    background: var(--white);
    transform: scale(0.8);
    transform-origin: 0 0;
    overflow: hidden;
  }
  .flyer--front { left: 40px; top: 212px; }
  .flyer--back { left: 616px; top: 214px; height: 960px; }
  .shapes { position: absolute; inset: 0; }
  .abs { position: absolute; }

  .brand { position: absolute; text-align: center; color: var(--red); font-weight: 800; line-height: 1.05; }
  .brand__mark { display: block; margin: 0 auto 10px; background: var(--red); }
  .brand__name { display: block; }

  .headline {
    left: 52px; top: 412px;
    font-size: 50px; font-weight: 800; color: var(--orange); letter-spacing: 0.5px;
    white-space: nowrap;
  }
  .price-line {
    left: 52px; top: 478px;
    font-size: 26px; font-weight: 600; color: var(--ink); white-space: nowrap;
  }
  .price { color: var(--orange); font-weight: 800; font-size: 30px; }
  .offer { position: absolute; left: 86px; font-size: 17px; font-weight: 600; line-height: 32px; white-space: nowrap; }
  .offer::before {
    content: ""; position: absolute; left: -30px; top: 9px;
    width: 14px; height: 14px; border-radius: 50%; background: var(--red);
  }
  .offer .price { font-size: 30px; }
  .offer--discount .price { font-size: 32px; }
  .terms { display: block; font-size: 9px; font-weight: 400; line-height: 10px; margin-top: -4px; margin-left: 2px; }
  .promise {
    left: 0; top: 690px; width: 680px; height: 62px;
    background: var(--orange); color: var(--white);
    font-size: 21px; font-weight: 800; line-height: 25px; padding: 6px 52px;
  }
  .thumbs { left: 60px; top: 770px; display: flex; gap: 10px; }
  .thumb { width: 182px; height: 102px; border: 2px solid var(--orange); }
  .thumb--keypad { background: linear-gradient(135deg, #7d8ca6, #dfe3ea 60%, #9aa0a8); }
  .thumb--panel { background: linear-gradient(135deg, #e6e6e6, #c9b9a4 70%, #8d7b66); }
  .thumb--kitchen { background: linear-gradient(135deg, #bfd2e6, #ededed 55%, #c9a98a); }

  .footer { position: absolute; left: 0; background: var(--dark); color: var(--white); }
  .flyer--front .footer { top: 888px; width: 680px; height: 77px; }
  .phone { position: absolute; font-weight: 800; color: var(--white); white-space: nowrap; }
  .contact { position: absolute; font-size: 15px; color: var(--white); white-space: nowrap; line-height: 20px; }
  .divider { position: absolute; width: 2px; background: var(--white); }

  .question {
    left: 32px; top: 16px; color: var(--white);
    font-size: 19px; font-weight: 800; line-height: 23px; text-transform: uppercase;
  }
  .points { list-style: none; }
  .point {
    position: absolute; left: 78px; width: 570px;
    font-size: 15px; line-height: 20px; color: var(--ink);
  }
  .point::before {
    content: ""; position: absolute; left: -28px; top: 4px;
    width: 12px; height: 12px; border-radius: 50%; background: var(--red);
  }
  .call-band {
    left: 0; top: 680px; width: 680px; height: 88px;
    background: var(--orange); color: var(--white);
    font-size: 17px; font-weight: 700; line-height: 24px; padding: 10px 44px;
    text-transform: uppercase;
  }
  .badge { position: absolute; top: 790px; text-align: center; font-size: 6px; line-height: 7px; color: var(--ink); }
  .badge__seal { display: block; margin: 0 auto 3px; width: 36px; height: 36px; border-radius: 50%; border: 3px solid #1e3d7a; background: #e9edf5; }
  .badge__cert { display: block; width: 36px; height: 46px; border: 2px solid #1e3d7a; background: #f3f3f3; }
  .badge__listing { display: block; width: 94px; height: 30px; border-radius: 4px; background: #f8e1d2; }
  .accredited {
    position: absolute; left: 368px; top: 821px; color: var(--white);
    font-size: 17px; font-weight: 700; white-space: nowrap;
  }
  .flyer--back .footer { top: 862px; width: 680px; height: 83px; }
  .follow { position: absolute; left: 362px; top: 55px; font-size: 14px; font-weight: 700; display: flex; align-items: center; gap: 7px; }
  .follow__dot { width: 15px; height: 15px; border-radius: 50%; background: var(--white); }
  .follow__label { margin-right: 4px; }
</style>
</head>
<body>

<section class="flyer flyer--front">
  <svg class="shapes" viewBox="0 0 680 965" width="680" height="965">
    <defs>
      <linearGradient id="keypadTone" x1="0" y1="0" x2="1" y2="1">
        <stop offset="0" stop-color="#c9ccd2"/>
        <stop offset="0.45" stop-color="#5d6f92"/>
        <stop offset="0.75" stop-color="#1d2230"/>
        <stop offset="1" stop-color="#d9d9d9"/>
      </linearGradient>
      <linearGradient id="appTone" x1="0" y1="0" x2="1" y2="1">
        <stop offset="0" stop-color="#3aa0e0"/>
        <stop offset="1" stop-color="#e8eef5"/>
      </linearGradient>
    </defs>
    <polygon points="0,0 680,0 680,215 340,400 0,215" fill="url(#keypadTone)" role="img" aria-label="Photo of a wall-mounted alarm keypad showing a welcome message"/>
    <polygon points="350,0 680,0 680,164 435,164" fill="#ffffff"/>
    <rect x="435" y="164" width="245" height="6" fill="var(--orange)"/>
    <polyline points="0,218 340,403 680,218" fill="none" stroke="var(--orange)" stroke-width="14"/>
    <polyline points="0,230 340,415 680,230" fill="none" stroke="var(--dark)" stroke-width="6"/>
    <polygon points="0,234 340,419 680,234 680,690 0,690" fill="#ffffff"/>
    <circle cx="525" cy="295" r="93" fill="#ffffff" stroke="var(--orange)" stroke-width="5"/>
    <circle cx="525" cy="295" r="85" fill="url(#appTone)" role="img" aria-label="Photo of two smartphones showing the alarm control app"/>
  </svg>

  <div class="brand" style="left:455px; top:16px; width:210px;">
    <span class="brand__mark" style="width:54px; height:54px;"></span>
    <span class="brand__name" style="font-size:31px;">K P GUARD</span>
    <span class="brand__name" style="font-size:31px;">SERVICES</span>
  </div>

  <h1 class="abs headline">K P GUARD SERVICES</h1>
  <p class="abs price-line">Intruder Alarms starting from <span class="price">£495</span> + VAT.</p>

  <p class="offer" style="top:526px;">Not happy with your current provider? Free of charge no<br>obligation take over survey and quotation and up to <span class="price">£100</span> off</p>
  <p class="offer offer--discount" style="top:596px;"><span class="price">£150 discount</span> on installations<span class="terms">*terms and conditions apply</span></p>
  <p class="offer" style="top:645px;">CCTV systems starting from <span class="price">£595</span> + VAT (based on 2 cameras)</p>

  <p class="abs promise">K P Guard Services are always there, always available, wherever and whenever you need us.</p>

  <div class="abs thumbs">
    <div class="thumb thumb--keypad" role="img" aria-label="Photo of an alarm keypad in a hallway"></div>
    <div class="thumb thumb--panel" role="img" aria-label="Photo of a hand using an alarm panel in a bedroom"></div>
    <div class="thumb thumb--kitchen" role="img" aria-label="Photo of a touchscreen alarm panel in a kitchen"></div>
  </div>

  <footer class="footer">
    <svg class="abs" style="left:52px; top:27px;" width="24" height="24" viewBox="0 0 24 24">
      <circle cx="12" cy="12" r="11" fill="none" stroke="#fff" stroke-width="2"/>
      <path d="M8 6.5l2 0 1 3-1.5 1c.7 1.6 1.9 2.8 3.5 3.5l1-1.5 3 1v2c0 .8-.7 1.3-1.5 1.2C10.5 16.2 7.8 13.5 7 8c-.1-.8.2-1.5 1-1.5z" fill="#fff"/>
    </svg>
    <span class="phone" style="left:86px; top:20px; font-size:27px;">01632 480913</span>
    <span class="divider" style="left:275px; top:12px; height:54px;"></span>
    <svg class="abs" style="left:292px; top:12px;" width="22" height="20" viewBox="0 0 22 20">
      <path d="M11 1L1 10h3v9h5v-6h4v6h5v-9h3z" fill="var(--orange)"/>
    </svg>
    <span class="contact" style="left:326px; top:12px;">14 Larkfield Road, Brentwood, Essex, CM99 1ZX</span>
    <svg class="abs" style="left:292px; top:46px;" width="22" height="16" viewBox="0 0 22 16">
      <rect x="0" y="0" width="22" height="16" fill="var(--orange)"/>
      <polyline points="0,0 11,9 22,0" fill="none" stroke="var(--dark)" stroke-width="1.5"/>
    </svg>
    <span class="contact" style="left:326px; top:44px;">operations@kpguardservices.co.uk</span>
  </footer>
</section>

<section class="flyer flyer--back">
  <svg class="shapes" viewBox="0 0 680 960" width="680" height="960">
    <defs>
      <linearGradient id="cameraTone" x1="0" y1="0" x2="1" y2="1">
        <stop offset="0" stop-color="#6d6259"/>
        <stop offset="0.4" stop-color="#2a2a2a"/>
        <stop offset="0.75" stop-color="#6f8b8f"/>
        <stop offset="1" stop-color="#a9bdbf"/>
      </linearGradient>
    </defs>
    <polygon points="0,80 405,80 458,165 680,165 680,237 360,357 0,217" fill="url(#cameraTone)" role="img" aria-label="Photo of a CCTV security camera mounted on a building"/>
    <polygon points="0,0 356,0 398,80 0,80" fill="var(--orange)"/>
    <polygon points="356,0 376,0 418,80 398,80" fill="var(--dark)"/>
    <polyline points="0,222 360,364 680,242" fill="none" stroke="var(--orange)" stroke-width="12"/>
    <polyline points="0,232 360,374 680,252" fill="none" stroke="#ffffff" stroke-width="4"/>
    <polygon points="372,800 680,800 680,860 340,860" fill="var(--orange)"/>
    <polygon points="270,945 680,945 680,960 255,960" fill="var(--orange)"/>
  </svg>

  <h2 class="abs question">Are you looking to keep<br>you and your premises safe?</h2>

  <div class="brand" style="left:482px; top:18px; width:170px;">
    <span class="brand__mark" style="width:50px; height:50px;"></span>
    <span class="brand__name" style="font-size:24px;">K P GUARD</span>
    <span class="brand__name" style="font-size:24px;">SERVICES</span>
  </div>

  <ul class="points">
    <li class="point" style="top:376px;">K P Guard Services install, maintain and repair all intruder<br>alarms, CCTV, intercom and access control</li>
    <li class="point" style="top:422px;">View, control and manage your security systems anywhere in the world</li>
    <li class="point" style="top:445px;">Feel at ease with monitoring services &amp; police response tailored to suit<br>you and your business</li>
    <li class="point" style="top:493px;">K P Guard can takeover any existing security system and offer maintenance<br>checks to guarantee the best performance for you and your premises</li>
    <li class="point" style="top:537px;">K P Guard understand that being security conscious is ever increasing,<br>protecting your property and family is a number one priority</li>
    <li class="point" style="top:584px;">Our fully insured and accredited team offer quality, safety and cost efficiency<br>throughout the whole process</li>
    <li class="point" style="top:629px;">K P Guard Services are using the latest cloud-based technology to stay<br>connected with your home and business 24/7</li>
  </ul>

  <p class="abs call-band">If you are looking to improve the security in your<br>home, office or commercial property then call a<br>member of our team today for a free quote.</p>

  <div class="badge" style="left:40px;"><span class="badge__seal"></span>CCTV<br>Systems</div>
  <div class="badge" style="left:104px;"><span class="badge__seal"></span>Intruder Alarm<br>Systems</div>
  <div class="badge" style="left:176px;"><span class="badge__cert"></span></div>
  <div class="badge" style="left:235px; top:803px;"><span class="badge__listing"></span></div>

  <p class="accredited">FULLY INSURED AND ACCREDITED</p>

  <footer class="footer">
    <svg class="abs" style="left:48px; top:15px;" width="22" height="22" viewBox="0 0 24 24">
      <circle cx="12" cy="12" r="11" fill="none" stroke="#fff" stroke-width="2"/>
      <path d="M8 6.5l2 0 1 3-1.5 1c.7 1.6 1.9 2.8 3.5 3.5l1-1.5 3 1v2c0 .8-.7 1.3-1.5 1.2C10.5 16.2 7.8 13.5 7 8c-.1-.8.2-1.5 1-1.5z" fill="#fff"/>
    </svg>
    <span class="phone" style="left:78px; top:5px; font-size:31px;">01632 480913</span>
    <svg class="abs" style="left:50px; top:55px;" width="22" height="16" viewBox="0 0 22 16">
      <rect x="0" y="0" width="22" height="16" fill="var(--orange)"/>
      <polyline points="0,0 11,9 22,0" fill="none" stroke="var(--dark)" stroke-width="1.5"/>
    </svg>
    <span class="contact" style="left:83px; top:53px; font-size:14px;">operations@kpguardservices.co.uk</span>
    <span class="divider" style="left:350px; top:6px; height:70px;"></span>
    <svg class="abs" style="left:362px; top:8px;" width="22" height="20" viewBox="0 0 22 20">
      <path d="M11 1L1 10h3v9h5v-6h4v6h5v-9h3z" fill="var(--orange)"/>
    </svg>
    <span class="contact" style="left:395px; top:6px;">14 Larkfield Road, Brentwood,<br>Essex, CM99 1ZX</span>
    <div class="follow">
      <span class="follow__label">Follow Us:</span>
      <span class="follow__dot"></span>
      <span class="follow__dot"></span>
      <span class="follow__dot"></span>
    </div>
  </footer>
</section>

</body>
</html>
```